M&A Advisory firm needs elegant and powerful letterhead

We need a powerful but elegant letterhead to engage with the international financial industry.

Target Market(s)

New York and International Financial Industry

Industry/Entity Type

Finance

Font styles to use
Other font styles liked:
• Poppins

Requirements
Must have
• 437 W 82nd Street 14th Floor New York, NY 10024 O: +1 (212) 555 0147 F: +1 (212) 555 0182

```html
<!DOCTYPE html>
<html lang="en">
<head>
<meta charset="UTF-8">
<title>Calvane Letterhead</title>
<link rel="stylesheet" href="https://fonts.googleapis.com/css2?family=Poppins:wght@400;500;600&display=swap">
<style>
  :root {
    --backdrop: #d9d9da;
    --paper: #f6f6f6;
    --navy: #1f4f99;
    --ink: #555a60;
    --ink-dark: #1c1f24;
    --rule-grey: #8a8a8a;
    --deco: #e2e2e2;
    --stamp: #5c82cf;
  }
  * { margin: 0; padding: 0; box-sizing: border-box; }
  html, body { width: 1200px; height: 800px; overflow: hidden; }
  body {
    background: var(--backdrop);
    font-family: "Poppins", sans-serif;
    display: flex; align-items: center; justify-content: center;
  }
  .letterhead {
    position: relative;
    width: 538px; height: 760px;
    background: var(--paper);
    box-shadow: 0 6px 18px rgba(0,0,0,0.12);
    overflow: hidden;
  }
  .brand {
    position: absolute; left: 46px; top: 46px;
    display: flex; align-items: center; gap: 10px;
  }
  .brand-dot {
    width: 26px; height: 26px; border-radius: 50%;
    background: var(--navy);
  }
  .brand-name {
    font-size: 27px; font-weight: 500; letter-spacing: 0.5px;
    color: var(--navy);
  }
  .decoration {
    position: absolute; right: -20px; top: 420px;
    width: 320px; height: 280px;
    background: radial-gradient(ellipse at 60% 45%, var(--deco) 0%, rgba(226,226,226,0.55) 40%, rgba(246,246,246,0) 70%);
  }
  .letter-block {
    position: absolute; left: 62px; top: 168px; width: 430px;
    font-size: 9.2px; line-height: 14px; color: var(--ink);
  }
  .letter-body p { margin-bottom: 14px; }
  .letter-body p:last-child { margin-bottom: 0; }
  .sign-off {
    position: relative; height: 96px; margin-top: 8px;
  }
  .closing {
    position: absolute; right: 0; top: 0;
  }
  .notary-seal {
    position: absolute; right: 14px; top: 22px;
    width: 66px; height: 66px; border-radius: 50%;
    border: 2px solid var(--stamp);
    box-shadow: inset 0 0 0 5px var(--paper), inset 0 0 0 6px var(--stamp);
  }
  .contact {
    position: absolute; left: 58px; top: 676px;
    font-size: 9.6px; font-weight: 500; color: var(--ink-dark);
  }
  .contact-row { display: flex; align-items: center; gap: 8px; height: 17px; }
  .contact-row svg { width: 9px; height: 9px; flex: none; }
  .label { color: var(--navy); font-weight: 600; }
  .gap { display: inline-block; width: 6px; }
  .footer-rule {
    position: absolute; left: 56px; right: 40px; top: 718px;
    height: 2px;
    background: linear-gradient(90deg, var(--navy) 0 46%, var(--rule-grey) 46% 100%);
  }
</style>
</head>
<body>
  <main class="letterhead">
    <header class="brand">
      <span class="brand-dot"></span>
      <span class="brand-name">CALVANE</span>
    </header>

    <div class="decoration" role="img" aria-label="Faint grey decorative motif of joined dots"></div>

    <section class="letter-block">
      <div class="letter-body">
        <p>Lorem ipsum dolor sit amet, consectetur adipiscing elit. Donec orci purus, luctus vitae dignissim eu, iaculis sed purus. Vivamus faucibus, ipsum nec aliquet viverra, leo mauris condimentum ligula, sit amet sagittis enim ligula quis arcu. Nam egestas tortor id nisi porttitor mattis. In tortor ante, ultricies in suscipit a, tempus non massa. Vivamus et auctor mi. Fusce vel massa nulla. Phasellus nec eros mauris, et scelerisque orci.</p>
        <p>Donec malesuada orci vitae nulla accumsan porta a id massa. Quisque accumsan iaculis magna sit amet fringilla. Maecenas consequat, magna eget tincidunt semper, odio nibh rutrum mi, id feugiat ante nisi eu risus. Vestibulum nunc orci, rhoncus a placerat in, ultricies in mi. Cras mattis varius eros, vel fringilla nisi suscipit eget. Quisque scelerisque sagittis nulla at porttitor.</p>
        <p>Sed id augue vitae urna euismod commodo aliquet a quam. Pellentesque arcu velit, cursus et malesuada ut, consequat et diam. Nullam erat sem, rhoncus id ullamcorper vitae, rhoncus et arcu. In ultricies ultricies nulla, ut rutrum nisi iaculis at. Donec eu magna a metus ornare faucibus. Fusce aliquet faucibus ultricies. Morbi semper, est id tincidunt gravida, sem arcu adipiscing lacus, ac bibendum nulla leo eu purus. Quisque nec diam sed risus consectetur a accumsan quis quis nibh. Vestibulum id purus lorem.</p>
      </div>
      <div class="sign-off">
        <div class="closing">Sincerely,</div>
        <div class="notary-seal" role="img" aria-label="Blue notary seal with signature"></div>
      </div>
    </section>

    <footer class="contact">
      <div class="contact-row">
        <svg viewBox="0 0 24 24" fill="none" stroke="#1f4f99" stroke-width="2.4"><path d="M5 3h4l2 5-3 2a12 12 0 0 0 6 6l2-3 5 2v4a2 2 0 0 1-2 2A17 17 0 0 1 3 5a2 2 0 0 1 2-2z"/></svg>
        <span><span class="label">O:</span> +1 (212) 555 0147<span class="gap"></span><span class="label">F:</span> +1 (212) 555 0182</span>
      </div>
      <div class="contact-row">
        <svg viewBox="0 0 24 24" fill="none" stroke="#1f4f99" stroke-width="2.4"><path d="M12 22s7-7 7-12a7 7 0 0 0-14 0c0 5 7 12 7 12z"/><circle cx="12" cy="10" r="2.5"/></svg>
        <span>437 W 82nd Street 14th Floor New York, NY 10024</span>
      </div>
    </footer>
    <div class="footer-rule"></div>
  </main>
</body>
</html>
```